IT-support company web-site design

We need to re-design out site for existing clients and for the future promotions. Site needs to be attractive with intuitive interface. We need to keep our logo and colors but any reshuffles can be made. I provide the working site and re-made version, which we do nt like. It has to be more bright and clear. All the blocks have to be divided and look like logic and structured. PLease find the addresses to work with below.
The "real" one https://plorim.com
The version http://dostuly.net/Plorim/
If you have any с

Industry/Entity Type

It Company

Number of Pages Required

5+ page

Font styles to use
Sans Serif

Colors
9bcb3c

Requirements
Must have
• Our LOGO and our colors (green palette). We d like to make our services blocks as the main things. We need to have our images and slogans as there are extremely important advantages of our company.
Nice to have
• Original and modern view of the site.
Should not have
• unpredictable and @surprising@, hard- definable buttons and ways

```html
<!DOCTYPE html>
<html lang="en">
<head>
<meta charset="utf-8">
<title>Plorim — IT Support</title>
<link rel="stylesheet" href="https://fonts.googleapis.com/css2?family=Mulish:wght@300;400;600;700&family=Open+Sans:ital,wght@0,400;0,600;1,400&display=swap">
<style>
:root{
  --green:#8cc63f;
  --green-light:#a6d35a;
  --green-dark:#6cb02c;
  --ink:#333;
  --text:#555;
  --muted:#999;
  --grey-bg:#efefef;
  --white:#fff;
  --line:#ddd;
}
*{box-sizing:border-box;margin:0;padding:0}
html,body{width:1200px;height:3255px;overflow:hidden}
body{font-family:"Mulish",sans-serif;color:var(--ink);background:var(--white);position:relative}
section,header,footer{position:absolute;left:0;width:1200px}

/* header */
.site-header{top:0;height:102px;background:var(--white)}
.brand{position:absolute;left:108px;top:32px;display:flex;align-items:center;gap:12px;font-size:34px;font-weight:300;color:var(--text);letter-spacing:1px}
.brand-dot{width:30px;height:30px;border:2px solid var(--green);border-radius:50%}
.main-nav{position:absolute;left:348px;top:50px;display:flex;gap:26px;font-size:16px;color:var(--text)}
.login{position:absolute;right:102px;top:0;width:82px;height:32px;background:var(--green);color:var(--white);font-size:12px;font-weight:700;text-align:center;line-height:32px}

/* hero */
.hero{top:102px;height:556px;background:linear-gradient(100deg,#3c4146 0%,#5a6066 45%,#44494e 70%,#2b3035 100%)}
.hero-title{position:absolute;top:178px;width:100%;text-align:center;color:var(--white);font-weight:600}
.hero-title .l1{display:block;font-size:37px;letter-spacing:.5px}
.hero-title .l2{display:block;font-size:50px;margin-top:-2px}
.btn-solid{position:absolute;left:528px;top:290px;width:168px;height:50px;background:var(--green);color:var(--white);font-size:16px;font-weight:600;text-align:center;line-height:50px;border-radius:2px}
.dots{position:absolute;top:517px;left:555px;display:flex;gap:8px}
.dots i{width:11px;height:11px;border-radius:50%;background:var(--white);display:block}
.dots i:first-child{outline:2px solid var(--white);outline-offset:2px;background:transparent}

/* about */
.about{top:658px;height:486px}
.about-photo{position:absolute;right:0;top:0;width:700px;height:486px;background:linear-gradient(90deg,rgba(255,255,255,1) 0%,rgba(220,225,230,.6) 25%,#b8c0c8 60%,#8d959e 100%)}
.about-text{position:absolute;left:122px;top:95px;width:470px}
.about-text h2{font-size:38px;font-weight:400;color:#444;margin-bottom:22px}
.about-text p{font-size:16px;line-height:1.65;color:var(--muted);margin-bottom:14px}
.btn-outline{display:inline-block;border:2px solid var(--green);color:var(--green);font-size:12px;font-weight:700;padding:9px 20px;text-transform:uppercase}
.about .btn-outline{margin-top:10px}

/* why */
.why{top:1144px;height:456px;background:linear-gradient(180deg,var(--green-light),var(--green-dark))}
.section-title{position:absolute;width:100%;text-align:center;font-size:30px;font-weight:400}
.why .section-title{top:44px;color:var(--white)}
.feature{position:absolute;top:110px;width:300px;text-align:center;color:var(--white)}
.feature svg{display:block;margin:0 auto}
.feature h3{font-size:19px;font-weight:600;line-height:1.25;margin-top:10px}
.feature p{font-size:11px;line-height:1.6;opacity:.9;margin:10px auto 0;width:230px}
.btn-white{display:inline-block;margin-top:14px;border:2px solid var(--white);color:var(--white);font-size:12px;font-weight:700;padding:9px 18px;background:rgba(255,255,255,.05)}

/* testimonials */
.testimonials{top:1600px;height:401px}
.testimonials .section-title{top:42px;color:#222}
.quote-card{position:absolute;top:110px;width:411px;height:182px;border:1px solid var(--line);box-shadow:0 2px 6px rgba(0,0,0,.08);background:var(--white);padding:26px 34px 0;text-align:center;font-family:"Open Sans",sans-serif;font-style:italic;font-size:13px;line-height:1.9;color:#444}
.avatar{position:absolute;top:160px;left:50%;margin-left:-37px;width:74px;height:74px;border-radius:50%;border:3px solid var(--white);background:linear-gradient(180deg,#c9b7a6,#8f7f70)}
.quote-name{position:absolute;top:336px;width:411px;text-align:center;font-family:"Open Sans",sans-serif;font-size:14px;color:#333}
.arrow{position:absolute}

/* callout */
.callout{top:2001px;height:464px;background:var(--grey-bg)}
.callout-photo{position:absolute;left:0;top:0;width:601px;height:464px;background:linear-gradient(135deg,#d9e4ee,#9fb2c4 55%,#6f8aa3)}
.callout-text{position:absolute;left:653px;top:82px;width:470px}
.callout-text h2{font-size:24px;font-weight:400;line-height:1.35;color:#222;margin-bottom:26px}
.ticks{list-style:none;font-size:13px;color:var(--muted)}
.ticks li{display:flex;align-items:center;gap:12px;height:34px}
.tick{width:16px;height:16px;border-radius:50%;background:var(--green);flex:none;display:flex;align-items:center;justify-content:center}
.callout .btn-outline{margin-top:28px;padding:9px 24px}

/* partners */
.partners{top:2465px;height:291px}
.partners .section-title{top:54px;color:#111}
.partner{position:absolute;top:148px;height:54px;display:flex;align-items:center;justify-content:center;text-align:center;font-weight:700;color:#333}

/* footer */
.site-footer{top:2756px;height:499px;background:var(--green)}
.footer-col{position:absolute;top:131px;color:var(--white)}
.footer-col h4{font-size:21px;font-weight:400;margin-bottom:18px}
.footer-col li{list-style:none;font-size:15px;line-height:32px}
.contact li{display:flex;gap:12px;align-items:flex-start;line-height:28px}
.socials{display:flex;gap:6px;margin-top:8px}
.socials i{width:28px;height:28px;border:2px solid var(--white);border-radius:50%;display:block}
.copyright{position:absolute;left:68px;right:68px;top:430px;border-top:1px solid rgba(255,255,255,.35);padding-top:16px;text-align:center;color:rgba(255,255,255,.8);font-size:14px}
</style>
</head>
<body>

<header class="site-header">
  <div class="brand"><span class="brand-dot"></span>PLORIM</div>
  <nav class="main-nav">
    <span>Plorim Difference</span><span>Services</span><span>Customers</span><span>Resources</span><span>Support</span><span>About Us</span><span>Contact Us</span>
  </nav>
  <div class="login">LOGIN</div>
</header>

<section class="hero" role="img" aria-label="Photo of two technicians with a laptop in a server room">
  <h1 class="hero-title"><span class="l1">WE MAKE YOUR INFORMATION TECHNOLOGY</span><span class="l2">SECURE AND SIMPLE</span></h1>
  <div class="btn-solid">READ MORE</div>
  <div class="dots"><i></i><i></i><i></i><i></i></div>
</section>

<section class="about">
  <div class="about-photo" role="img" aria-label="Photo of a man working at a desk with two monitors"></div>
  <div class="about-text">
    <h2>About Our Company</h2>
    <p>Sed ut perspiciatis unde omnis iste natus error sit voluptatem accusantium doloremque</p>
    <p>inventore veritatis et quasi architecto beatae vitae dicta sunt explicabo. Nemo enim ipsam voluptatem quia voluptas sit aspernatur aut odit aut fugit, sed quia consequuntu</p>
    <span class="btn-outline">Read more ⊕</span>
  </div>
</section>

<section class="why">
  <h2 class="section-title">WHY WE ARE</h2>
  <div class="feature" style="left:150px">
    <svg width="140" height="110" viewBox="0 0 140 110" fill="none" stroke="rgba(255,255,255,.6)" stroke-width="2"><path d="M30 95a24 24 0 0 1 0-48 34 34 0 0 1 64-14 26 26 0 0 1 16 62z"/><g stroke="#fff" stroke-width="4" stroke-linecap="round"><path d="M52 42l38 38"/><path d="M90 42L52 80"/></g></svg>
    <h3>Freedom from<br>IT Worries</h3>
    <p>Sed ut perspiciatis unde omnis iste natus error sit voluptatem accusantium</p>
    <span class="btn-white">READ MORE ⊕</span>
  </div>
  <div class="feature" style="left:432px">
    <svg width="140" height="110" viewBox="0 0 140 110" fill="none" stroke="rgba(255,255,255,.6)" stroke-width="2"><path d="M30 95a24 24 0 0 1 0-48 34 34 0 0 1 64-14 26 26 0 0 1 16 62z"/><text x="70" y="82" text-anchor="middle" font-family="Mulish,sans-serif" font-size="54" font-weight="700" fill="#fff" stroke="none">$</text></svg>
    <h3>Eliminate Unpredictable<br>IT Expenses. Reduce IT Costs</h3>
    <p>Sed ut perspiciatis unde omnis iste natus error sit voluptatem accusantium</p>
    <span class="btn-white">READ MORE ⊕</span>
  </div>
  <div class="feature" style="left:779px">
    <svg width="140" height="110" viewBox="0 0 140 110" fill="none" stroke="rgba(255,255,255,.6)" stroke-width="2"><path d="M30 95a24 24 0 0 1 0-48 34 34 0 0 1 64-14 26 26 0 0 1 16 62z"/><g stroke="#fff" stroke-width="4" stroke-linecap="round"><path d="M48 66V56a22 22 0 0 1 44 0v10"/><rect x="44" y="60" width="10" height="16" rx="3"/><rect x="86" y="60" width="10" height="16" rx="3"/><path d="M91 76q0 10-14 10"/></g></svg>
    <h3>Houston-based 24/7<br>Help Desk Support</h3>
    <p>Sed ut perspiciatis unde omnis iste natus error sit voluptatem accusantium</p>
    <span class="btn-white">READ MORE ⊕</span>
  </div>
</section>

<section class="testimonials">
  <h2 class="section-title">TESTIMONIALS</h2>
  <svg class="arrow" style="left:128px;top:192px" width="24" height="44" viewBox="0 0 24 44"><path d="M20 4L4 22l16 18" fill="none" stroke="#bbb" stroke-width="4"/></svg>
  <svg class="arrow" style="left:1044px;top:192px" width="24" height="44" viewBox="0 0 24 44"><path d="M4 4l16 18L4 40" fill="none" stroke="#bbb" stroke-width="4"/></svg>
  <div class="quote-card" style="left:169px">“We didn't have the expertise or resources to keep our network up-to- date with ever-growing record keeping and patient privacy regulations. With Tidelink®, I can focus on running my practice”<div class="avatar" role="img" aria-label="Client portrait"></div></div>
  <div class="quote-card" style="left:618px">“As an e-retailer, our business relies on our computer system. We're no longer bogged down by computer downtime or security threats. With Tidelink®, I can focus on growing my business”<div class="avatar" role="img" aria-label="Client portrait"></div></div>
  <div class="quote-name" style="left:169px">Corwin D. Halley MD,PA</div>
  <div class="quote-name" style="left:618px">Marcus Elden, Executive VP</div>
</section>

<section class="callout">
  <div class="callout-photo" role="img" aria-label="Photo of a smiling support agent wearing a headset"></div>
  <div class="callout-text">
    <h2>Lower your total IT costs with Plorim’s simple flat fee structure so you can focus on growing your business.</h2>
    <ul class="ticks">
      <li><span class="tick"><svg width="10" height="8" viewBox="0 0 10 8"><path d="M1 4l3 3 5-6" fill="none" stroke="#fff" stroke-width="2"/></svg></span>Massa erat pretium arcu, nec eleifend.</li>
      <li><span class="tick"><svg width="10" height="8" viewBox="0 0 10 8"><path d="M1 4l3 3 5-6" fill="none" stroke="#fff" stroke-width="2"/></svg></span>Nullam lorem enim, faucibus a turpis eu luctus.</li>
      <li><span class="tick"><svg width="10" height="8" viewBox="0 0 10 8"><path d="M1 4l3 3 5-6" fill="none" stroke="#fff" stroke-width="2"/></svg></span>Aenean sit amet lobortis metus. In tempor dui et hendrerit.</li>
      <li><span class="tick"><svg width="10" height="8" viewBox="0 0 10 8"><path d="M1 4l3 3 5-6" fill="none" stroke="#fff" stroke-width="2"/></svg></span>Nullam lorem enim, faucibus a turpis eu luctus.</li>
    </ul>
    <span class="btn-outline">Read more</span>
  </div>
</section>

<section class="partners">
  <h2 class="section-title">OUR PARTNERS</h2>
  <svg class="arrow" style="left:68px;top:150px" width="22" height="58" viewBox="0 0 22 58"><path d="M20 2L3 29l17 27" fill="none" stroke="#aaa" stroke-width="2"/></svg>
  <svg class="arrow" style="left:1100px;top:150px" width="22" height="58" viewBox="0 0 22 58"><path d="M2 2l17 27L2 56" fill="none" stroke="#aaa" stroke-width="2"/></svg>
  <div class="partner" style="left:118px;width:130px;font-size:26px">VERANDEL</div>
  <div class="partner" style="left:296px;width:180px;font-size:20px">Keep Lindale Green</div>
  <div class="partner" style="left:520px;width:140px;font-size:20px">KRT Associates</div>
  <div class="partner" style="left:718px;width:140px;font-size:16px">BRIGHTVALE</div>
  <div class="partner" style="left:896px;width:180px;font-size:16px;font-weight:400">Reach Onward</div>
</section>

<footer class="site-footer">
  <svg style="position:absolute;left:0;top:0" width="1200" height="70" viewBox="0 0 1200 70"><path d="M0 0h1200v6L600 66 0 6z" fill="#fff"/><path d="M0 6l600 60 600-60" fill="none" stroke="#555" stroke-width="6"/></svg>
  <div class="footer-col" style="left:98px"><h4>Company</h4><ul><li>Core Benefits</li><li>Side by Side Comparison</li><li>vs. IT Consultants</li><li>vs. In-house</li><li>vs. Outsourcing</li></ul></div>
  <div class="footer-col" style="left:354px"><h4>Our Services</h4><ul><li>Upfront Audit</li><li>Service Types</li><li>Moving to Plorim System</li><li>Cost Savings</li><li>Performance Tracking</li></ul></div>
  <div class="footer-col" style="left:634px"><h4>Resources</h4><ul><li>FAQ's</li><li>Helpful Tips</li><li>White Papers</li><li>Brochures</li><li>Booklets</li></ul></div>
  <div class="footer-col contact" style="left:872px"><h4>Contact Us</h4><ul>
    <li><svg width="14" height="20" viewBox="0 0 14 20" style="margin-top:4px"><path d="M7 0a7 7 0 0 1 7 7c0 5-7 13-7 13S0 12 0 7a7 7 0 0 1 7-7z" fill="#fff"/><circle cx="7" cy="7" r="2.5" fill="#8cc63f"/></svg><span>245 Orchard Lane #4B<br>Texas 75001 TX</span></li>
    <li><svg width="16" height="16" viewBox="0 0 16 16" style="margin-top:6px"><path d="M3 1l3 3-2 2q2 4 6 6l2-2 3 3-2 2Q5 14 1 3z" fill="none" stroke="#fff" stroke-width="1.6"/></svg><span>555.014.2290</span></li>
    <li><svg width="16" height="14" viewBox="0 0 16 14" style="margin-top:7px"><rect x="1" y="1" width="14" height="12" fill="none" stroke="#fff" stroke-width="1.6"/><path d="M1 1l7 6 7-6" fill="none" stroke="#fff" stroke-width="1.6"/></svg><span>info@plorim.com</span></li>
  </ul>
  <div class="socials"><i></i><i></i><i></i><i></i></div></div>
  <div class="copyright">© 2017 Company Name. All right reserved</div>
</footer>

</body>
</html>
```